Wordpress Design for my Consulting Company

We want a WordPress site created for our new business. We have created a mock-up of the content we want on the site at https://marcobellweather.example.com/website-5

We are not attached to any of the pictures and just put stock stuff from bloq's editor, which we don't have rights to use outside of bloq.

We are NOT looking to just port this site to WordPress, we are looking for some creative ways to display the content in a more professional artistic sense.

I have included several logo files and a text file with the colors and Fonts used in the logo. We are not looking to change the logo or the colors used in the logo.

The Schedule appointment links to a page that embeds a bookslot.example calendar. https://bookslot.example.com/marco-bellweather/trailguide

The final website domain will be venturelanterns.example

Venture lanterns is a consulting company that works directly with the business owners and leaders of small businesses between 50-200 employees. We help companies make sure they have the right technology to meet their strategic goals. We are the anti-"Computer Guy" and we focus on business outcomes NOT cool technology gadgets.

The final design should communicate business growth and success.

Target Market(s)

Business Owners of companies with 50-200 employees

Coding

Coded - Design and coding required

Number of Pages Required

1 page

Font styles to use
Serif
Other font styles liked:
• Trajan Pro Bold, Open Sans

Requirements
Must have
• Should focus on consulting rather than technology.
• Should show the customer as the hero and we are just their guide.
• Must use the logo provided and the colors and fonts in the text file provided. Any other colors and fonts must be complementary.
• The design should scale for all devices computer, iPad, or phone
Should not have
• Should not focus on technology, we are the anti-"Computer Guy" and we focus on business outcomes NOT cool technology gadgets.

```html
<!DOCTYPE html>
<html lang="en">
<head>
<meta charset="utf-8">
<title>Venture Lanterns — Technology Advisors</title>
<link href="https://fonts.googleapis.com/css2?family=Roboto:wght@400;500;700;900&family=Open+Sans:wght@400;600&display=swap" rel="stylesheet">
<style>
:root{
  --copper:#c8774a;
  --copper-soft:#d39b7a;
  --slate:#2f4450;
  --slate-band:#3e535c;
  --ink:#333;
  --muted:#777;
  --white:#fff;
  --paper:#fff;
}
*{box-sizing:border-box;margin:0;padding:0}
html,body{width:1200px;height:2980px;overflow:hidden;background:var(--paper)}
body{position:relative;font-family:"Open Sans",Arial,sans-serif;color:var(--ink)}
.abs{position:absolute}
.heading{font-family:"Roboto",Arial,sans-serif;font-weight:900;color:var(--slate);letter-spacing:-.5px;line-height:1.2}
.eyebrow{font-family:"Roboto",Arial,sans-serif;font-weight:400;color:var(--copper);letter-spacing:3px;font-size:15px}
.copy{font-size:11px;line-height:17px;color:var(--muted)}
.btn-outline{border:2px solid var(--slate);border-radius:20px;font:700 10px "Roboto",sans-serif;letter-spacing:1.5px;color:var(--slate);display:flex;align-items:center;justify-content:center}
.btn-copper{background:var(--copper);color:var(--white);border-radius:30px;font:700 11px "Roboto",sans-serif;letter-spacing:1px;display:flex;align-items:center;justify-content:center}

/* header */
.site-header{top:0;left:0;width:1200px;height:116px;background:var(--white)}
.brand-mark{left:175px;top:14px;width:80px;height:80px;border-radius:50%;background:var(--copper)}
.brand-name{left:272px;top:38px;font:700 24px/30px "Roboto",sans-serif;color:var(--slate);letter-spacing:2px}
.main-nav{top:44px;left:596px;display:flex;gap:44px;font:500 12px "Roboto",sans-serif;color:#333;letter-spacing:.5px}
.nav-cta{left:868px;top:32px;width:160px;height:40px;border:2px solid var(--copper);border-radius:22px;font:500 11px "Roboto",sans-serif;color:#333;display:flex;align-items:center;justify-content:center}

/* hero */
.hero{top:116px;left:0;width:1200px;height:570px;background:linear-gradient(100deg,#9a8a7c 0%,#d8d4cc 35%,#e9ecec 55%,#8c8e92 80%,#3c3c40 100%)}
.hero-kicker{left:175px;top:400px;font:700 17px/20px "Roboto",sans-serif;color:var(--white)}
.hero-title{left:172px;top:418px;font:900 50px/60px "Roboto",sans-serif;color:var(--white);letter-spacing:-.5px}
.hero-sub{left:175px;top:478px;font:400 14px/18px "Roboto",sans-serif;color:var(--white)}
.hero-cta{left:175px;top:523px;width:200px;height:51px}
.slider-arrows{left:173px;top:648px;width:80px;height:38px;display:flex;background:var(--white)}
.slider-arrows span{flex:1;display:flex;align-items:center;justify-content:center;border:1px solid #ddd}

/* welcome */
.welcome-photo{left:686px;top:739px;width:364px;height:237px;background:linear-gradient(90deg,#e8e4e0,#cfd6de 50%,#b8c2cc)}
.welcome-eyebrow{left:175px;top:736px}
.welcome-title{left:172px;top:750px;font-size:44px}
.welcome-copy{left:175px;top:810px;width:488px}
.learn-more{width:106px;height:32px}

/* achieve */
.achieve-eyebrow{left:175px;top:1052px}
.achieve-title{left:175px;top:1069px;font-size:35px}
.achieve-rule{left:501px;top:1053px;width:2px;height:52px;background:var(--copper)}
.achieve-copy{left:528px;top:1056px;width:500px}

/* four steps */
.steps-band{top:1184px;left:0;width:1200px;height:496px;background:var(--slate-band)}
.steps-kicker{top:1234px;left:0;width:1200px;text-align:center;font:700 12px/14px "Roboto",sans-serif;color:var(--white)}
.steps-title{top:1250px;left:0;width:1200px;text-align:center;font:900 56px/66px "Roboto",sans-serif;color:var(--white);letter-spacing:-1px}
.steps-intro{top:1324px;left:255px;width:690px;text-align:center;font-size:11px;line-height:17px;color:var(--white)}
.step-title{font:700 17px/22px "Roboto",sans-serif;color:var(--white)}
.step-copy{font-size:11px;line-height:16px;color:var(--white);width:310px}
.step-left{text-align:right}
.step-icon{width:72px;height:72px;border-radius:50%;border:2px solid var(--white);display:flex;align-items:center;justify-content:center}
.step-icon i{width:56px;height:56px;border-radius:50%;background:var(--white);display:flex;align-items:center;justify-content:center}

/* meeting */
.meeting-eyebrow{top:1728px;left:0;width:1200px;text-align:center}
.meeting-title{top:1742px;left:0;width:1200px;text-align:center;font-size:44px}
.meeting-intro{top:1806px;left:255px;width:690px;text-align:center}
.calendar-frame{left:173px;top:1893px;width:855px;height:239px;border:3px solid var(--slate)}
.calendar-label{left:540px;top:1878px;width:120px;background:var(--white);text-align:center;font:700 23px/30px "Roboto",sans-serif;color:var(--copper)}
.calendar-sub{top:1910px;left:0;width:1200px;text-align:center;font:400 19px/22px "Roboto",sans-serif;color:var(--slate)}
.day{top:1965px;width:88px;height:88px;border:3px solid var(--slate);text-align:center;font-family:"Roboto",sans-serif;color:var(--slate);background:var(--white)}
.day b{display:block;margin-top:24px;font-size:14px}
.day span{font-size:12px}
.day.is-active{background:var(--copper);border-color:var(--copper);color:var(--white)}
.cal-arrow{top:1992px;width:30px;height:30px;background:var(--copper);display:flex;align-items:center;justify-content:center}
.week-btn{top:2114px;width:123px;height:34px;font-weight:400}

/* connect */
.connect-band{top:2222px;left:0;width:1200px;height:154px;background:linear-gradient(180deg,#4d4d4d,#6b6763)}
.connect-title{top:2254px;left:0;width:1200px;text-align:center;font:900 44px/52px "Roboto",sans-serif;color:var(--white);letter-spacing:-1px}
.social-row{top:2314px;left:523px;display:flex;gap:4px}
.social-row i{width:31px;height:31px;border-radius:5px;background:var(--white)}

/* form */
.field{border:1.5px solid #bbb;border-radius:26px;font:400 12px "Roboto",sans-serif;color:#999;padding:0 22px;display:flex;align-items:center;letter-spacing:.5px}
.field.message{align-items:flex-start;padding-top:20px;border-radius:40px}
.submit{left:515px;top:2657px;width:188px;height:46px;background:var(--copper-soft);color:var(--white);border-radius:24px;font:700 16px "Roboto",sans-serif;letter-spacing:1px;display:flex;align-items:center;justify-content:center}

/* footer info */
.info-title{top:2774px;font:700 18px/22px "Roboto",sans-serif;color:var(--slate)}
.info-text{font-size:11px;line-height:16px;color:#555}
.quick-links{left:830px;top:2815px;width:220px;display:flex;flex-wrap:wrap;gap:6px 24px;font-size:11px;color:#444}
.legal-bar{top:2925px;left:0;width:1200px;height:55px;background:var(--copper-soft);text-align:center;font:700 11px/55px "Roboto",sans-serif;color:var(--white);letter-spacing:.5px}
</style>
</head>
<body>

<header class="abs site-header">
  <div class="abs brand-mark"></div>
  <div class="abs brand-name">VENTURE LANTERNS</div>
  <nav class="abs main-nav"><span>HOME</span><span>ABOUT US</span><span>SERVICES</span></nav>
  <div class="abs nav-cta">SCHEDULE APPOINTMENT</div>
</header>

<section class="abs hero" role="img" aria-label="Photo of four business people talking around a meeting table"></section>
<div class="abs hero-kicker">TECHNOLOGY ADVISORS</div>
<h1 class="abs hero-title">THAT "GET" BUSINESS.</h1>
<p class="abs hero-sub">We help you leverage technology to create a competitive advantage.</p>
<div class="abs btn-copper hero-cta">SCHEDULE APPOINTMENT</div>
<div class="abs slider-arrows">
  <span><svg width="10" height="16" viewBox="0 0 10 16"><path d="M8 1 2 8l6 7" fill="none" stroke="#999" stroke-width="1.5"/></svg></span>
  <span><svg width="10" height="16" viewBox="0 0 10 16"><path d="M2 1l6 7-6 7" fill="none" stroke="#999" stroke-width="1.5"/></svg></span>
</div>

<section>
  <div class="abs eyebrow welcome-eyebrow">WELCOME TO</div>
  <h2 class="abs heading welcome-title">LANTERNS</h2>
  <div class="abs copy welcome-copy">
    <p>Curabitur imperdiet eros in neque pellentesque dignissim. Maecenas sit amet dui magna. Ut porttitor augue turpis, maximus rhoncus purus pretium vitae. Fusce purus odio, volutpat a ex in, scelerisque tincidunt quam. Aliquam euismod cursus nisl vitae pretium. Aliquam iaculis euismod mi at suscipit. Ut id urna nisi Maecenas sit amet dui magna.</p>
    <p style="margin-top:16px">Maecenas molestie id velit a rhoncus. Sed porttitor enim leo. Quisque auctor ultricies lacinia. Sed et purus vehicula, convallis risus vitae.</p>
  </div>
  <div class="abs btn-outline learn-more" style="left:173px;top:946px">LEARN MORE</div>
  <div class="abs welcome-photo" role="img" aria-label="Photo of a doctor in a white coat talking with a client"></div>
</section>

<section>
  <div class="abs eyebrow achieve-eyebrow">HELPING ASSOCIATES TO</div>
  <h2 class="abs heading achieve-title">ACHIEVE SUCCESS</h2>
  <div class="abs achieve-rule"></div>
  <p class="abs copy achieve-copy">Lorem Ipsum is simply dummy text of the printing and typesetting industry. Lorem Ipsum has been the industry's standard dummy text ever since the 1500s, when an unknown printer .</p>
  <div class="abs btn-outline learn-more" style="left:922px;top:1107px">LEARN MORE</div>
</section>

<section class="abs steps-band" role="img" aria-label="Dimmed photo of a team meeting in an office"></section>
<div class="abs steps-kicker">TO YOUR BUSINESS STRATEGY !</div>
<h2 class="abs steps-title">THE FOUR STEPS</h2>
<p class="abs steps-intro">Lorem Ipsum is simply dummy text of the printing and typesetting industry. Lorem Ipsum has been the industry's standard dummy text ever since the 1500s, when an unknown printer took a galley of type and scrambled</p>

<div class="abs step-left" style="left:160px;top:1412px;width:310px">
  <div class="step-title">DISCOVER</div>
  <p class="step-copy">Outside of learning how to use a certain language or technology, each course will focus on scenarios where those languages or technologies apply.</p>
</div>
<div class="abs step-icon" style="left:489px;top:1413px"><i><svg width="28" height="28" viewBox="0 0 28 28"><circle cx="14" cy="12" r="8" fill="none" stroke="#c8774a" stroke-width="2"/><path d="M14 20v5" stroke="#c8774a" stroke-width="2"/></svg></i></div>

<div class="abs step-icon" style="left:638px;top:1413px"><i><svg width="28" height="28" viewBox="0 0 28 28"><rect x="6" y="4" width="16" height="20" fill="none" stroke="#c8774a" stroke-width="2"/><path d="M10 10h8M10 15h8M10 20h5" stroke="#c8774a" stroke-width="2"/></svg></i></div>
<div class="abs" style="left:727px;top:1412px">
  <div class="step-title">IMPLEMENT</div>
  <p class="step-copy">Outside of learning how to use a certain language or technology, each course will focus on scenarios where those languages or technologies apply.</p>
</div>

<div class="abs step-left" style="left:160px;top:1522px;width:310px">
  <div class="step-title">PRIORITIZE</div>
  <p class="step-copy">If you think for one second that you will just hear ramblings from the tutor and that is it, you have got to be joking. Before you are done you will be challenged</p>
</div>
<div class="abs step-icon" style="left:489px;top:1522px"><i><svg width="28" height="28" viewBox="0 0 28 28"><rect x="4" y="5" width="20" height="15" fill="none" stroke="#c8774a" stroke-width="2"/><path d="M9 16v-4M14 16V9M19 16v-6M10 24h8" stroke="#c8774a" stroke-width="2"/></svg></i></div>

<div class="abs step-icon" style="left:638px;top:1522px"><i><svg width="28" height="28" viewBox="0 0 28 28"><rect x="4" y="6" width="20" height="14" rx="2" fill="none" stroke="#c8774a" stroke-width="2"/><circle cx="14" cy="13" r="3" fill="none" stroke="#c8774a" stroke-width="2"/><path d="M10 24h8" stroke="#c8774a" stroke-width="2"/></svg></i></div>
<div class="abs" style="left:727px;top:1522px">
  <div class="step-title">MAINTAIN</div>
  <p class="step-copy">If you think for one second that you will just hear ramblings from the tutor and that is it, you have got to be joking. Before you are done you will be challenged</p>
</div>

<section>
  <div class="abs eyebrow meeting-eyebrow">MEETING</div>
  <h2 class="abs heading meeting-title">LANTERNS</h2>
  <p class="abs copy meeting-intro">Lorem Ipsum is simply dummy text of the printing and typesetting industry. Lorem Ipsum has been the industry's standard dummy text ever since the 1500s, when an unknown printer took a galley of type and scrambled</p>
  <div class="abs calendar-frame"></div>
  <div class="abs calendar-label">TODAY</div>
  <div class="abs calendar-sub">SELECT A DAY</div>
  <div class="abs cal-arrow" style="left:157px"><svg width="8" height="12" viewBox="0 0 8 12"><path d="M6 1 1 6l5 5" fill="none" stroke="#fff" stroke-width="2"/></svg></div>
  <div class="abs cal-arrow" style="left:1012px"><svg width="8" height="12" viewBox="0 0 8 12"><path d="M2 1l5 5-5 5" fill="none" stroke="#fff" stroke-width="2"/></svg></div>
  <div class="abs day" style="left:203px"><b>MON</b><span>NOV 28</span></div>
  <div class="abs day" style="left:320px"><b>TUE</b><span>NOV 28</span></div>
  <div class="abs day is-active" style="left:439px"><b>WED</b><span>NOV 28</span></div>
  <div class="abs day" style="left:556px"><b>THU</b><span>NOV 28</span></div>
  <div class="abs day" style="left:676px"><b>FRI</b><span>NOV 28</span></div>
  <div class="abs day" style="left:793px"><b>SAT</b><span>NOV 28</span></div>
  <div class="abs day" style="left:910px"><b>SUN</b><span>NOV 28</span></div>
  <div class="abs btn-copper week-btn" style="left:509px">THIS WEEK</div>
  <div class="abs btn-copper week-btn" style="left:640px">NEXT WEEK</div>
</section>

<section class="abs connect-band" role="img" aria-label="Dimmed photo of a city skyline"></section>
<h2 class="abs connect-title">CONNECT WITH US</h2>
<div class="abs social-row" aria-label="Social links"><i></i><i></i><i></i><i></i></div>

<form>
  <div class="abs field" style="left:173px;top:2422px;width:420px;height:50px">NAME</div>
  <div class="abs field" style="left:610px;top:2422px;width:418px;height:50px">EMAIL</div>
  <div class="abs field" style="left:173px;top:2482px;width:855px;height:50px">PHONE NUMBER</div>
  <div class="abs field message" style="left:173px;top:2545px;width:855px;height:82px">MESSAGE</div>
  <div class="abs submit">SUBMIT</div>
</form>

<footer>
  <h3 class="abs info-title" style="left:173px">CONTACT DETAILS</h3>
  <svg class="abs" style="left:171px;top:2818px" width="20" height="28" viewBox="0 0 20 28"><path d="M10 1C5 1 1 5 1 10c0 7 9 17 9 17s9-10 9-17c0-5-4-9-9-9z" fill="#c8774a"/><circle cx="10" cy="10" r="3.5" fill="#fff"/></svg>
  <p class="abs info-text" style="left:202px;top:2818px">418 Harbor Mill Road South,<br>Fairview Bend, TX 70000</p>

  <h3 class="abs info-title" style="left:536px">PHONE NUMBER</h3>
  <svg class="abs" style="left:536px;top:2818px" width="30" height="30" viewBox="0 0 30 30"><rect width="30" height="30" rx="4" fill="#d39b7a"/><path d="M9 7c2 0 3 3 3 4s-2 1-1 3 3 4 5 5 2-1 3-1 4 1 4 3-2 3-4 3C13 24 6 17 6 10c0-2 1-3 3-3z" fill="#fff"/></svg>
  <p class="abs" style="left:576px;top:2825px;font-size:14px;color:#555">+ 01234 567890</p>

  <h3 class="abs info-title" style="left:830px">QUICK LINK</h3>
  <nav class="abs quick-links"><span>Home</span><span>About Us</span><span>Services</span><span>Schedule Appointment</span></nav>

  <div class="abs legal-bar">© 2018 VENTURE LANTERNS. ALL RIGHT RESERVED.</div>
</footer>

</body>
</html>
```